The Lantern Guide

I am a life coach specializing in helping people with depression and bipolar disorder. I would like a nice, fun design for a business card.

```html
<!DOCTYPE html>
<html lang="en">
<head>
<meta charset="utf-8">
<title>The Lantern Guide – Business Card</title>
<link rel="stylesheet" href="https://fonts.googleapis.com/css2?family=Montserrat:wght@600&family=Open+Sans:wght@400&display=swap">
<style>
  :root {
    --page-bg: #e9e7e3;
    --card-bg: #fbfbfb;
    --brand-blue: #1f8fcf;
    --deep-blue: #1672b8;
    --light-blue: #45b3dc;
    --accent-orange: #f07a33;
    --text-dark: #3a3a3a;
  }
  * { margin: 0; padding: 0; box-sizing: border-box; }
  html, body { width: 1200px; height: 1022px; overflow: hidden; background: var(--page-bg); }
  .card {
    position: absolute; left: 75px; top: 211px;
    width: 1050px; height: 600px;
    background: linear-gradient(160deg, #ffffff 0%, var(--card-bg) 60%, #eeeeee 100%);
    border-radius: 26px; overflow: hidden;
    box-shadow: 0 18px 40px rgba(0,0,0,0.18);
    font-family: "Open Sans", sans-serif;
    color: var(--text-dark);
  }
  .card__swoosh { position: absolute; inset: 0; }
  .brand-name {
    position: absolute; left: 70px; top: 240px;
    font-size: 52px; font-weight: 400; color: var(--brand-blue);
    letter-spacing: 0.5px; white-space: nowrap;
  }
  .divider {
    position: absolute; left: 580px; top: 150px;
    width: 2px; height: 280px; background: var(--accent-orange);
  }
  .contact { position: absolute; left: 612px; top: 120px; }
  .contact__name {
    font-family: "Montserrat", sans-serif; font-weight: 600;
    font-size: 38px; color: var(--brand-blue); letter-spacing: 1px; line-height: 1.1;
  }
  .contact__role { font-size: 21px; margin-top: 4px; }
  .contact__address { font-size: 21px; line-height: 1.45; margin-top: 22px; }
  .contact__list { list-style: none; margin-top: 16px; font-size: 21px; line-height: 1.5; }
  .contact__list li { display: flex; align-items: center; gap: 12px; }
  .contact__list svg { width: 16px; height: 16px; flex: none; }
  .web-domain { color: var(--brand-blue); }
</style>
</head>
<body>
  <div class="card">
    <svg class="card__swoosh" viewBox="0 0 1050 600" preserveAspectRatio="none" aria-hidden="true">
      <defs>
        <linearGradient id="bandGrad" x1="0" y1="0" x2="1" y2="0">
          <stop offset="0" stop-color="var(--light-blue)"/>
          <stop offset="1" stop-color="var(--deep-blue)"/>
        </linearGradient>
      </defs>
      <path d="M0 600 L0 520 C300 560 700 540 1050 450 L1050 600 Z" fill="url(#bandGrad)"/>
      <path d="M180 505 C520 520 820 480 1050 405" fill="none" stroke="var(--accent-orange)" stroke-width="7"/>
      <path d="M180 512 C520 528 820 490 1050 418" fill="none" stroke="#ffffff" stroke-width="6"/>
    </svg>

    <div class="brand-name">The Lantern Guide</div>
    <div class="divider"></div>

    <div class="contact">
      <div class="contact__name">DANIEL HARTLEY</div>
      <div class="contact__role">Director</div>
      <div class="contact__address">Harbour Lane,<br>Glenmore NSW, Australia</div>
      <ul class="contact__list">
        <li><svg viewBox="0 0 16 16"><path d="M4 1 L6 5 L4.5 6.5 C5.5 8.5 7.5 10.5 9.5 11.5 L11 10 L15 12 L13.5 15 C7 14.5 1.5 9 1 2.5 Z" fill="var(--accent-orange)"/></svg>0491570156</li>
        <li><svg viewBox="0 0 16 16"><rect x="4" y="1" width="8" height="14" rx="1.5" fill="none" stroke="var(--accent-orange)" stroke-width="1.6"/></svg>0491570110</li>
        <li><svg viewBox="0 0 16 16"><rect x="1" y="3" width="14" height="10" fill="none" stroke="var(--accent-orange)" stroke-width="1.6"/><path d="M1 3 L8 9 L15 3" fill="none" stroke="var(--accent-orange)" stroke-width="1.6"/></svg>info@thelanternguide.com</li>
        <li><svg viewBox="0 0 16 16"><circle cx="8" cy="8" r="6.5" fill="none" stroke="var(--accent-orange)" stroke-width="1.5"/><path d="M1.5 8 H14.5 M8 1.5 C5 5 5 11 8 14.5 C11 11 11 5 8 1.5" fill="none" stroke="var(--accent-orange)" stroke-width="1.2"/></svg>www.<span class="web-domain">thelanternguide</span>.com</li>
      </ul>
    </div>
  </div>
</body>
</html>
```